Business Card for Spa
Stationary
Project: Business Card for Spa
Business Card for Spa - Salon & Spa
Creative Brief
Use specific fonts
Use both logo font and standard fonts
Professional
Lotus Drift
Relaxing Beautiful Healthy
418 Brambleford Road Suite 210 Maple Crossing, OR 70914
info@lotusdriftwellness.example
www.lotusdriftwellness.example
Lic. # MT573160
Mobile: Health Fairs Private Events Corporate Events
Swedish - Deep Tissue - Hot Stone - Prenatal - Chair Massage - 4 Hand Massage -Ayus Lomi Lomi - Aromatherapy Salt Glow Scrub - Sports Massage - Facials All Natural Body Wraps & Scrubs for De-Aging Exfoliation - Body Aches - Weight Loss

```html
<!DOCTYPE html>
<html lang="en">
<head>
<meta charset="utf-8">
<title>Lotus Drift – Business Card</title>
<link href="https://fonts.googleapis.com/css2?family=Lato:wght@400;700&display=swap" rel="stylesheet">
<style>
  :root {
    --teal: #2bb3b6;
    --teal-mid: #7fd0d2;
    --teal-light: #bfe7e8;
    --brown: #7a3a2c;
    --ink: #5e5e5e;
    --paper: #ffffff;
    --backdrop: #e9ecec;
  }
  * { box-sizing: border-box; margin: 0; padding: 0; }
  html, body { width: 1200px; height: 901px; overflow: hidden; }
  body {
    background: var(--backdrop);
    font-family: "Lato", sans-serif;
    position: relative;
  }
  .card {
    position: absolute;
    width: 540px;
    height: 309px;
    background: var(--paper);
    border-radius: 14px;
    overflow: hidden;
    box-shadow: 0 6px 18px rgba(0,0,0,0.12);
  }

  /* Back side */
  .card-back { left: 40px; top: 296px; }
  .services {
    position: absolute;
    left: 26px; top: 36px;
    width: 300px;
    color: var(--ink);
    font-size: 11.5px;
    line-height: 1.5;
  }
  .services-title { color: var(--teal); font-weight: 700; font-size: 12.5px; margin-bottom: 4px; }
  .services p + p { margin-top: 10px; }
  .petal-area {
    position: absolute;
    right: 0; top: 0;
    width: 230px; height: 200px;
    background: radial-gradient(circle 220px at 100% 0%, var(--teal) 0%, var(--teal-mid) 40%, var(--teal-light) 68%, rgba(255,255,255,0) 100%);
  }
  .back-brand {
    position: absolute;
    right: 36px; top: 212px;
    color: var(--brown);
    font-size: 18px;
    font-weight: 700;
    letter-spacing: 0.5px;
  }

  /* Front side */
  .card-front { left: 620px; top: 296px; }
  .brand {
    position: absolute;
    left: 40px; top: 100px;
    display: flex; align-items: center; gap: 12px;
  }
  .brand-dot { width: 22px; height: 22px; border-radius: 50%; background: var(--teal); }
  .brand-name { color: var(--brown); font-size: 34px; font-weight: 700; letter-spacing: 1px; }
  .contact {
    position: absolute;
    left: 300px; top: 52px;
    color: var(--ink);
    font-size: 11.5px;
    line-height: 1.45;
  }
  .contact-name { color: var(--teal); font-weight: 700; font-size: 13px; }
  .contact-tagline { font-size: 10.5px; margin-bottom: 12px; }
  .contact-address { margin-bottom: 12px; }
  .contact-lines { display: grid; grid-template-columns: 16px auto; column-gap: 6px; align-items: center; }
  .contact-lines svg { width: 12px; height: 12px; fill: var(--teal); }
  .rule { position: absolute; left: 0; right: 0; bottom: 44px; height: 3px; background: var(--brown); }
  .footer-band {
    position: absolute; left: 0; right: 0; bottom: 0;
    height: 38px;
    background: var(--teal);
    color: var(--paper);
    font-size: 12px;
    letter-spacing: 2px;
    display: flex; align-items: center; justify-content: center;
  }
</style>
</head>
<body>

<section class="card card-back">
  <div class="petal-area" role="img" aria-label="Soft teal layered petal decoration"></div>
  <div class="services">
    <p class="services-title">Specialist in:</p>
    <p>Swedish - Deep Tissue - Hot Stone - Prenatal<br>Chair Massage - 4 Hand Massage - Ayus Lomi Lomi<br>Aromatherapy Salt Glow Scrub - Sports Massage<br>Facials</p>
    <p>All Natural Body Wraps &amp; Scrubs for De-Aging<br>Exfoliation - Body Aches - Weight Loss</p>
    <p>Mobile: Health Fairs<br>Private Events<br>Corporate Events</p>
  </div>
  <p class="back-brand">Lotus Drift</p>
</section>

<section class="card card-front">
  <div class="brand">
    <span class="brand-dot"></span>
    <span class="brand-name">Lotus Drift</span>
  </div>
  <div class="contact">
    <p class="contact-name">Lotus Drift</p>
    <p class="contact-tagline">Relaxing Beautiful Healthy</p>
    <p class="contact-address">418 Brambleford Road<br>Suite 210<br>Maple Crossing, OR 70914</p>
    <div class="contact-lines">
      <svg viewBox="0 0 24 24"><path d="M6.6 10.8a15 15 0 0 0 6.6 6.6l2.2-2.2a1 1 0 0 1 1-.25 11.4 11.4 0 0 0 3.6.57 1 1 0 0 1 1 1V20a1 1 0 0 1-1 1A17 17 0 0 1 3 4a1 1 0 0 1 1-1h3.5a1 1 0 0 1 1 1c0 1.25.2 2.45.57 3.6a1 1 0 0 1-.25 1z"/></svg>
      <span>888-555-0162</span>
      <svg viewBox="0 0 24 24"><path d="M7 2h10a2 2 0 0 1 2 2v16a2 2 0 0 1-2 2H7a2 2 0 0 1-2-2V4a2 2 0 0 1 2-2zm0 3v13h10V5zm5 14.2a1 1 0 1 0 0 .01z"/></svg>
      <span>281-555-0148</span>
      <svg viewBox="0 0 24 24"><path d="M3 5h18a1 1 0 0 1 1 1v12a1 1 0 0 1-1 1H3a1 1 0 0 1-1-1V6a1 1 0 0 1 1-1zm1 2.3V17h16V7.3l-8 5.2z"/></svg>
      <span>info@lotusdriftwellness.example</span>
    </div>
  </div>
  <div class="rule"></div>
  <div class="footer-band">www.lotusdriftwellness.example</div>
</section>

</body>
</html>
```